MS Word and MS Powerpoint template creation using existing logo as style guide

Create a professional looking MS Word document template and MS powerpoint template for Corvant Advisory Pty Ltd using a logo that's already been created as the style guide. Corvant is a professional services business providing strategy, governance and execution support to small and medium business, Boards and executive teams. refer design brief.

Target Market(s)

Small to medium business, Chairs, Boards, executive teams, general managers

Industry/Entity Type

Professional business services, consultancy, business support outsourcing

Other font styles liked:
• calibri

Requirements
Must have
• leverage the existing logo for colour scheme. Use the CORVANT logo type font. Fully editable templates Word and MS Powerpoint,
Nice to have
• Refer to the design brief
Should not have
• animations, cartoons, stock images of people.

```html
<!DOCTYPE html>
<html lang="en">
<head>
<meta charset="utf-8">
<title>Corvant Advisory – Board Presentation &amp; Document Templates</title>
<link rel="stylesheet" href="https://fonts.googleapis.com/css2?family=Cinzel:wght@400;500;600&family=Carlito:wght@400;700&display=swap">
<style>
  :root{
    --navy:#1d3350;
    --navy-deep:#142540;
    --navy-mid:#2c4a6e;
    --steel:#3e5f84;
    --gold:#c9a45c;
    --paper:#faf8f3;
    --ink:#2a2f38;
    --ink-soft:#5b6270;
    --rule:#d9d3c6;
    --backdrop:#ebe7e0;
  }
  *{box-sizing:border-box;margin:0;padding:0}
  html,body{width:1200px;height:691px;overflow:hidden;background:var(--backdrop)}
  body{position:relative;font-family:'Carlito',Calibri,sans-serif;color:var(--ink)}

  /* ---------- Presentation title slide ---------- */
  .slide{
    position:absolute;left:350px;top:18px;width:500px;height:282px;
    background:linear-gradient(135deg,var(--navy-mid) 0%,var(--navy) 45%,var(--navy-deep) 100%);
    overflow:hidden;box-shadow:0 2px 10px rgba(20,37,64,.25);
  }
  .slide__feature{
    position:absolute;right:0;top:0;width:200px;height:100%;
    background:linear-gradient(100deg,rgba(62,95,132,0) 0%,rgba(62,95,132,.55) 55%,rgba(201,164,92,.28) 100%);
  }
  .slide__content{position:absolute;left:0;right:0;top:88px;text-align:center;color:#fff}
  .wordmark{font-family:'Cinzel',serif;font-weight:500;letter-spacing:.14em;color:var(--gold)}
  .slide__wordmark{font-size:38px;line-height:1}
  .slide__entity{font-family:'Cinzel',serif;font-size:9px;letter-spacing:.08em;color:#e8e2d4;margin-top:8px}
  .slide__title{font-family:'Cinzel',serif;font-size:23px;letter-spacing:.03em;margin-top:18px;color:#f3efe6}
  .slide__tagline{font-size:11px;letter-spacing:.06em;text-transform:uppercase;margin-top:6px;color:#e8e2d4}

  /* ---------- Shared document styles ---------- */
  .doc{position:absolute;background:var(--paper);box-shadow:0 2px 10px rgba(20,37,64,.18);overflow:hidden}
  .doc__header{text-align:center}
  .doc__wordmark{font-size:26px;line-height:1;color:var(--navy)}
  .doc__tagline{font-family:'Cinzel',serif;font-size:8.5px;letter-spacing:.06em;color:var(--ink-soft);margin-top:4px;text-transform:uppercase}
  .doc__goldrule{height:2px;background:var(--gold);margin:6px 0 4px}
  .band{background:var(--navy);color:#fff;font-family:'Cinzel',serif;letter-spacing:.1em;text-align:center}

  /* ---------- Letter ---------- */
  .letter{left:92px;top:322px;width:600px;height:360px;padding:16px 46px}
  .letter .band{font-size:12px;padding:3px 0}
  .letter__meta{margin-top:9px;font-size:9.5px;line-height:1.3}
  .letter__meta .label{font-weight:700}
  .letter__subject{display:flex;gap:40px;font-size:9.5px;margin:6px 0 5px}
  .letter__subject .label{font-weight:700}
  .letter__body{font-size:9.5px;line-height:1.3}
  .letter__body p{margin-bottom:4px}
  .letter__body ul{margin:0 0 4px 20px}
  .letter__body .two-col{display:grid;grid-template-columns:1fr 1fr;column-gap:20px}

  /* ---------- Report ---------- */
  .report{left:718px;top:322px;width:448px;height:360px;padding:16px 30px}
  .report .doc__wordmark{font-size:24px}
  .report .band{font-size:11px;padding:3px 0}
  .report__fields{display:grid;grid-template-columns:1fr 1fr;gap:1px 20px;font-size:9px;margin:6px 0 7px;color:var(--ink-soft)}
  .report__section{margin-bottom:6px}
  .report__section-title{background:var(--navy);color:#fff;font-size:9.5px;font-weight:700;padding:2px 8px;letter-spacing:.04em}
  .report__row{display:flex;justify-content:space-between;font-size:9px;padding:2px 8px;border-bottom:1px solid var(--rule);color:var(--ink)}
  .report__row span:last-child{color:var(--ink-soft)}
</style>
</head>
<body>

<section class="slide" aria-label="Board presentation title slide">
  <div class="slide__feature" role="img" aria-label="Decorative navy and gold diagonal graphic area"></div>
  <div class="slide__content">
    <div class="wordmark slide__wordmark">CORVANT</div>
    <div class="slide__entity">CORVANT ADVISORY PTY LTD</div>
    <div class="slide__title">BOARD PRESENTATION</div>
    <div class="slide__tagline">Connecting Strategy, Governance &amp; Execution</div>
  </div>
</section>

<article class="doc letter" aria-label="Letter template">
  <header class="doc__header">
    <div class="wordmark doc__wordmark">CORVANT</div>
    <div class="doc__tagline">Connecting Strategy, Governance &amp; Execution</div>
    <div class="doc__goldrule"></div>
    <div class="band">CORVANT ADVISORY</div>
  </header>
  <div class="letter__meta">
    <div class="label">Date</div>
    <div class="label">To</div>
    <div>Client Name</div>
    <div>Client Organisation Pty Ltd</div>
    <div>Street Address, Suburb State 3000</div>
  </div>
  <div class="letter__subject"><span class="label">Subject</span><span>Connecting Strategy, Governance Support</span></div>
  <div class="letter__body">
    <p>Dear Management,</p>
    <p>Thank you for the opportunity to present our advisory proposal. This letter outlines how we support your board and executive team with strategy, governance and execution planning.</p>
    <ul>
      <li>First, a review of current strategy and board reporting cycles.</li>
      <li>Second, a structured governance framework aligned to your goals.</li>
      <li>Third, clear execution plans and progress reporting at each review.</li>
    </ul>
    <p>We only commit to clear outcomes, and our management support is practical:</p>
    <ul class="two-col">
      <li>Strategy insights</li>
      <li>Governance support</li>
      <li>Performance metrics</li>
      <li>Personal contact</li>
    </ul>
    <p>Contact us with simple questions at any time about your company.</p>
  </div>
</article>

<article class="doc report" aria-label="Report template">
  <header class="doc__header">
    <div class="wordmark doc__wordmark">CORVANT</div>
    <div class="doc__tagline">Connecting Strategy, Governance &amp; Execution</div>
    <div class="doc__goldrule"></div>
    <div class="band">REPORT</div>
  </header>
  <div class="report__fields">
    <span>Prepared for</span><span>Prepared by</span>
    <span>Client Name</span><span>Corvant Advisory Pty Ltd</span>
    <span>Date</span><span>Reference</span>
  </div>
  <div class="report__section">
    <div class="report__section-title">Executive Summary</div>
    <div class="report__row"><span>Purpose of report</span><span>1</span></div>
    <div class="report__row"><span>Key findings overview</span><span>2</span></div>
  </div>
  <div class="report__section">
    <div class="report__section-title">Strategic Context</div>
    <div class="report__row"><span>Market position</span><span>3</span></div>
    <div class="report__row"><span>Board priorities</span><span>4</span></div>
  </div>
  <div class="report__section">
    <div class="report__section-title">Governance Review</div>
    <div class="report__row"><span>Decision rights</span><span>5</span></div>
    <div class="report__row"><span>Reporting cadence</span><span>6</span></div>
  </div>
  <div class="report__section">
    <div class="report__section-title">Execution Plan</div>
    <div class="report__row"><span>Milestones</span><span>7</span></div>
    <div class="report__row"><span>Responsibilities</span><span>8</span></div>
  </div>
</article>

</body>
</html>
```